Back Pain

Need a flyer similar to the attached draft. This is to be handed out to prospective patients. Note that Sketch Hive has already designed the logo. If you need a copy please contact me

```html
<!DOCTYPE html>
<html lang="en">
<head>
<meta charset="utf-8">
<title>Tech Neck – Spine Ease Clinic</title>
<link rel="stylesheet" href="https://fonts.googleapis.com/css2?family=Oswald:wght@400;500;600&family=Open+Sans:wght@400;600;700&display=swap">
<style>
  :root {
    --blue: #2266ad;
    --blue-dark: #1b4f8a;
    --green: #7bbf43;
    --green-dark: #4f9a2f;
    --red: #a11d1d;
    --grey-text: #3e5670;
    --skin: #e9b89a;
    --teal: #1f8e95;
    --trouser: #707075;
    --page: #ffffff;
    --rule: #d8d8d8;
  }
  * { margin: 0; padding: 0; box-sizing: border-box; }
  html, body { width: 1200px; height: 1200px; overflow: hidden; background: #ffffff; }
  .flyer { position: relative; width: 1200px; height: 1200px; font-family: "Open Sans", Arial, sans-serif; }
  .page-edge {
    position: absolute; left: 170px; top: 16px; width: 860px; height: 1168px;
    background: var(--page); border: 1px solid var(--rule);
    box-shadow: 0 2px 6px rgba(0,0,0,0.12);
  }
  .brand { position: absolute; left: 0; top: 56px; width: 1200px; text-align: center; }
  .brand-mark { display: block; width: 64px; height: 64px; margin: 0 auto 6px; border-radius: 50%; background: var(--green); }
  .brand-name { display: block; font-family: "Oswald", sans-serif; font-weight: 600; font-size: 28px; line-height: 1.1; color: var(--blue); letter-spacing: 0.5px; }
  .brand-tag { display: block; font-family: "Oswald", sans-serif; font-weight: 600; font-size: 13px; line-height: 1.2; color: var(--blue); letter-spacing: 1px; }
  .title {
    position: absolute; left: 0; top: 200px; width: 1200px; text-align: center;
    font-family: "Oswald", sans-serif; font-weight: 600; font-size: 70px; line-height: 1.1;
    color: var(--blue); letter-spacing: 1px;
  }
  .figure {
    position: absolute; left: 186px; top: 296px; width: 112px; height: 754px;
    border-radius: 56px 56px 20px 20px;
    background: linear-gradient(180deg, #8a5a3c 0%, var(--skin) 12%, var(--teal) 22%, var(--teal) 38%, var(--trouser) 44%, var(--trouser) 95%, #2f2f33 100%);
  }
  .symptom {
    position: absolute; height: 28px; line-height: 28px; padding: 0 12px 0 22px;
    font-family: "Oswald", sans-serif; font-weight: 500; font-size: 17px;
    color: #fff; letter-spacing: 0.5px; white-space: nowrap;
  }
  .symptom::before { content: ""; position: absolute; left: 0; top: 0; width: 10px; height: 100%; background: var(--blue-dark); }
  .symptom.green { background: var(--green); }
  .symptom.blue { background: var(--blue); }
  .symptom.blue::before { background: var(--green-dark); }
  .chart-heading {
    position: absolute; left: 708px; top: 322px; width: 300px;
    font-family: "Oswald", sans-serif; font-weight: 500; font-size: 21px; line-height: 1.15;
    color: var(--blue);
  }
  .chart { position: absolute; left: 670px; top: 370px; }
  .pie { position: absolute; left: 606px; top: 636px; }
  .stat { position: absolute; left: 716px; top: 636px; font-family: "Oswald", sans-serif; white-space: nowrap; }
  .stat-line { font-weight: 500; color: var(--blue); font-size: 21px; line-height: 1.2; }
  .stat-big { font-weight: 600; color: var(--green); font-size: 37px; line-height: 1.1; }
  .pitch { position: absolute; left: 444px; top: 770px; font-family: "Oswald", sans-serif; font-weight: 600; white-space: nowrap; }
  .pitch span { display: block; line-height: 1.08; }
  .pitch .l1 { font-size: 38px; }
  .pitch .l2 { font-size: 28px; }
  .pitch .l3 { font-size: 36px; }
  .b { color: var(--blue); }
  .g { color: var(--green); }
  .address { position: absolute; left: 340px; width: 520px; top: 980px; text-align: center; color: var(--grey-text); font-size: 20px; line-height: 1.5; }
  .divider { position: absolute; left: 400px; top: 1060px; width: 400px; border-top: 2px dotted #8a8a8a; }
  .offer { position: absolute; left: 300px; width: 600px; top: 1074px; text-align: center; }
  .offer-head { font-weight: 700; font-size: 25px; line-height: 1.3; color: var(--red); }
  .offer-note { font-size: 15px; color: #333; line-height: 1.5; }
</style>
</head>
<body>
<main class="flyer">
  <div class="page-edge"></div>

  <header class="brand">
    <span class="brand-mark"></span>
    <span class="brand-name">SPINE EASE CLINIC</span>
    <span class="brand-tag">DR SAM HARLOW - CHIROPRACTOR</span>
  </header>

  <h1 class="title">TECH NECK</h1>

  <div class="figure" role="img" aria-label="Illustration of a woman bent over looking down at her phone, with her upper spine highlighted"></div>

  <div class="symptom green" style="left:400px; top:326px;">HEADACHES</div>
  <div class="symptom green" style="left:410px; top:374px;">NECK PAIN</div>
  <div class="symptom green" style="left:310px; top:424px; padding-left:70px;">SHOULDER PAIN</div>
  <div class="symptom blue" style="left:310px; top:462px; padding-left:54px;">BACK PAIN</div>
  <div class="symptom green" style="left:380px; top:554px;">ARM &amp; HAND PAIN</div>
  <div class="symptom blue" style="left:330px; top:636px; padding-left:34px;">SCIATICA</div>

  <p class="chart-heading">AS THE HEAD TILTS FORWARD<br>MORE FORCE IS PLACED<br>ON THE SPINE</p>

  <svg class="chart" width="340" height="240" viewBox="0 0 340 240" aria-label="Bar chart of pressure on spine by degrees of forward head tilt">
    <rect x="12" y="86" width="34" height="72" rx="14" fill="#2266ad" role="img" aria-label="Head profile silhouette"/>
    <g fill="#7bbf43">
      <rect x="60" y="120" width="36" height="50"/>
      <rect x="110" y="94" width="36" height="76"/>
      <rect x="160" y="66" width="36" height="104"/>
      <rect x="210" y="36" width="36" height="134"/>
      <rect x="260" y="10" width="36" height="160"/>
    </g>
    <g font-family="Oswald, sans-serif" font-size="16" fill="#ffffff" text-anchor="middle">
      <text x="78" y="150">12</text>
      <text x="128" y="124">27</text>
      <text x="178" y="96">40</text>
      <text x="228" y="66">49</text>
      <text x="278" y="40">60</text>
    </g>
    <g font-family="Oswald, sans-serif" font-weight="500" font-size="17" fill="#2266ad" text-anchor="middle">
      <text x="78" y="198">0°</text>
      <text x="128" y="198">15°</text>
      <text x="178" y="198">30°</text>
      <text x="228" y="198">45°</text>
      <text x="278" y="198">60°</text>
      <text x="180" y="228" font-size="16">DEGREES OF FORWARD HEAD TILT</text>
    </g>
    <text transform="translate(318 90) rotate(90)" font-family="Oswald, sans-serif" font-weight="500" font-size="13" fill="#2266ad" text-anchor="middle">PRESSURE ON SPINE (LBS)</text>
  </svg>

  <svg class="pie" width="88" height="88" viewBox="0 0 88 88" aria-label="Pie chart of daily screen time">
    <circle cx="44" cy="44" r="42" fill="#7bbf43"/>
    <path d="M44 44 L44 2 A42 42 0 0 1 74 73 Z" fill="#2266ad"/>
  </svg>
  <div class="stat">
    <div class="stat-line">THE AVERAGE PERSON SPENDS</div>
    <div class="stat-big">8-11 HOURS PER DAY</div>
    <div class="stat-line">USING ELECTRONIC DEVICES</div>
  </div>

  <p class="pitch">
    <span class="l1"><span class="b" style="display:inline">CHIROPRACTIC CARE</span> <span class="g" style="display:inline">CAN HELP</span></span>
    <span class="l2 g">CORRECT AND PREVENT THESE PROBLEMS</span>
    <span class="l3"><span class="b" style="display:inline">BY RESTORING</span> <span class="g" style="display:inline">AND</span> <span class="b" style="display:inline">MAINTAINING</span></span>
    <span class="l3"><span class="b" style="display:inline">PROPER ALIGNMENT</span> <span class="g" style="display:inline">OF THE</span> <span class="b" style="display:inline">NECK</span></span>
  </p>

  <p class="address">Dr. Samuel Harlow - Now in Portsmere at:<br>42 Harbour Rd., Quay Suites</p>

  <div class="divider"></div>

  <div class="offer">
    <p class="offer-head">50% OFF INITIAL CONSULTATION</p>
    <p class="offer-note">if you book online at www.spineeaseclinic.example<br>choose tech neck option</p>
  </div>
</main>
</body>
</html>
```